Building certification business in Sydney Australia

Brookvale Assessors is a small business that is currently growing and needs a profession looking website to attract customers and give them all the information they need. The main services we offer currently are pre-purchase building inspections for purchasers and other areas of construction consultancy including pool fencing certificates. Please see attached logos to incorporate to also match colour schemes with. Thanks!

Target Market(s)

Prospective buyers and home owners

Industry/Entity Type

Small Business

Requirements
Must have
• Promote the main services from the home page. Being able to select the type of service/certificate required from the main page and be directed to a specific page that deals with only that service containing the relevant information for that item.
Nice to have
• Small emphasis on the location of our office and areas we service etc.

```html
<!DOCTYPE html>
<html lang="en">
<head>
<meta charset="utf-8">
<title>Brookvale Assessors</title>
<link href="https://fonts.googleapis.com/css2?family=PT+Sans:ital,wght@0,400;0,700;1,400;1,700&display=swap" rel="stylesheet">
<style>
:root{
  --page-bg:#ebebeb;
  --white:#ffffff;
  --ink:#1e1e1e;
  --text:#6b6b6b;
  --blue:#1f7bbf;
  --icon-blue:#2f86c6;
  --topbar:#3b3b3b;
  --footer:#262626;
  --footer-bottom:#323232;
  --footer-text:#8c8c8c;
  --footer-line:#3d3d3d;
  --panel:#eeeeee;
}
*{box-sizing:border-box;margin:0;padding:0}
html,body{width:842px;height:1200px;overflow:hidden}
body{background:var(--page-bg);font-family:"PT Sans",Arial,sans-serif;color:var(--text);position:relative}
.site{position:absolute;left:80px;top:0;width:682px;height:1200px;background:var(--white)}
.topbar{height:24px;background:var(--topbar);display:flex;align-items:center;gap:16px;padding-left:30px;font-size:9px;color:#a8a8a8}
.topbar span,.bottom-bar span{display:flex;align-items:center;gap:5px}
.header{height:54px;position:relative}
.brand-name{position:absolute;left:24px;top:17px;font-size:21px;font-weight:700;color:var(--blue);line-height:1}
.nav{position:absolute;right:30px;top:26px;display:flex;gap:12px;font-size:10px;color:#666;align-items:center}
.nav .active{color:var(--blue)}
.hero{position:absolute;left:0;top:78px;width:682px;height:264px;background:linear-gradient(100deg,#d8d3c8 0%,#c9c4bb 35%,#7e8a92 55%,#dfe2e2 80%,#f0f0ee 100%)}
.hero-title{position:absolute;left:19px;top:229px;background:var(--blue);color:#fff;font-weight:700;font-style:italic;font-size:23px;line-height:28px;padding:6px 14px;height:40px}
.hero-tag{position:absolute;left:19px;top:270px;width:325px;height:32px;background:rgba(255,255,255,.85);font-size:8px;font-style:italic;color:#666;padding:11px 14px}
.welcome{position:absolute;left:29px;top:382px;width:624px;height:85px;background:var(--panel);border-left:3px solid var(--blue);padding:21px 17px}
.welcome h2{font-size:11px;color:var(--ink);font-weight:700;margin-bottom:4px}
.welcome p{font-size:8px;line-height:13px;width:470px}
.btn{position:absolute;right:20px;top:24px;width:80px;height:26px;background:var(--blue);color:#fff;font-size:9px;font-weight:700;display:flex;align-items:center;justify-content:center;border-radius:2px}
.services{position:absolute;left:29px;top:500px;width:624px;display:flex}
.service{width:156px;text-align:center;padding:0 10px}
.service svg{display:block;margin:0 auto 6px}
.service h3{font-size:11px;color:var(--ink);font-weight:700;line-height:16px;margin-bottom:5px}
.service p{font-size:8px;line-height:12px}
.service a{display:block;margin-top:7px;font-size:8px;color:var(--blue);text-decoration:none}
.contact{position:absolute;left:29px;top:714px;width:624px}
.contact h2{font-size:14px;color:var(--ink);font-weight:700;margin-bottom:12px}
.contact-row{display:flex;font-size:8px;line-height:12px}
.contact-row div:nth-child(1){width:90px}
.contact-row div:nth-child(2){width:96px}
.contact-row div:nth-child(3){width:155px}
.map{position:absolute;left:29px;top:802px;width:624px;height:165px;background:linear-gradient(135deg,#e8e4d8,#ddd8c8 60%,#b9cfe6 100%)}
.map-caption{position:absolute;right:29px;top:969px;font-size:8px;color:#666}
.footer{position:absolute;left:0;top:990px;width:682px;height:175px;background:var(--footer);display:flex;padding:34px 29px 0;gap:34px}
.footer-col{width:180px}
.footer-col:first-child{width:195px}
.footer-col h4{color:#eee;font-size:10px;font-weight:700;margin-bottom:14px}
.footer-col p{font-size:8px;line-height:12px;color:var(--footer-text)}
.footer-menu{list-style:none}
.footer-menu li{font-size:8px;color:var(--footer-text);padding:3px 6px 5px;border-bottom:1px solid var(--footer-line)}
.bottom-bar{position:absolute;left:0;top:1165px;width:682px;height:35px;background:var(--footer-bottom);display:flex;justify-content:center;align-items:center;gap:16px;font-size:9px;font-weight:700;color:#b5b5b5}
.to-top{position:absolute;left:796px;top:886px;width:26px;height:26px;background:#b2b2b2;border-radius:2px;display:flex;align-items:center;justify-content:center}
</style>
</head>
<body>
<div class="site">
  <div class="topbar">
    <span><svg width="7" height="10" viewBox="0 0 7 10"><rect x="0.5" y="0.5" width="6" height="9" rx="1" fill="none" stroke="#2f86c6"/></svg>(07) 5550 1842</span>
    <span><svg width="10" height="7" viewBox="0 0 10 7"><rect width="10" height="7" fill="#2f86c6"/><path d="M0 0 5 4 10 0" stroke="#3b3b3b" fill="none"/></svg>office@brookvaleassessors.com.au</span>
    <span><svg width="7" height="10" viewBox="0 0 7 10"><path d="M3.5 10 0.5 4a3 3 0 1 1 6 0z" fill="#2f86c6"/></svg>Harbourline Business Centre 58 Keel Street, Qld 4700 Australia</span>
  </div>
  <header class="header">
    <div class="brand-name">Brookvale Assessors</div>
    <nav class="nav"><span class="active">HOME</span><span>ABOUT US</span><span>OUR SERVICES</span><span>CONTACT US</span>
      <svg width="9" height="9" viewBox="0 0 9 9"><circle cx="3.6" cy="3.6" r="2.8" fill="none" stroke="#888" stroke-width="1.2"/><path d="M5.6 5.6 8.5 8.5" stroke="#888" stroke-width="1.3"/></svg></nav>
  </header>
  <div class="hero" role="img" aria-label="Photo of two smiling building inspectors in suits holding yellow hard hats outside a stone office building"></div>
  <div class="hero-title">BROOKVALE ASSESSORS</div>
  <div class="hero-tag">We are professional and cost effective in the delivery of our prompt customized services.</div>

  <section class="welcome">
    <h2>WELCOME</h2>
    <p>Brookvale Assessors offer pre-purchase building inspections for purchasers and other areas of construction consultancy including pool fencing certificates.</p>
    <div class="btn">READ MORE</div>
  </section>

  <section class="services">
    <div class="service">
      <svg width="34" height="34" viewBox="0 0 34 34"><path d="M5 3h18v26H5z" fill="none" stroke="#111" stroke-width="2.5"/><path d="M9 9h10M9 13h10M9 17h8M9 21h6" stroke="#111" stroke-width="2"/><path d="M17 24l4 4 10-11" fill="none" stroke="#111" stroke-width="3"/></svg>
      <h3>PRE-PURCHASE BUILDING INSPECTIONS</h3>
      <p>Getting a pre-purchase building inspection done can help you avoid purchasing a building with major structural issues – saving you major financial and emotional heartache down the track.</p>
      <a>Read more</a>
    </div>
    <div class="service">
      <svg width="34" height="34" viewBox="0 0 34 34"><circle cx="8" cy="5" r="3.5" fill="#111"/><circle cx="26" cy="5" r="3.5" fill="#111"/><path d="M4 10h8v10h-2v12H6V20H4zM22 10h8v10h-2v12h-4V20h-2z" fill="#111"/><path d="M12 15h10" stroke="#111" stroke-width="2.5"/><rect x="25" y="22" width="8" height="6" fill="#111"/></svg>
      <h3>CONSTRUCTION CONSULTANCY</h3>
      <p>Lorem ipsum dolor sit amet, consectetur adipiscing elit, sed do eiusmod tempor incididunt ut labore et dolore magna aliqua. Ut enim ad minim veniam, quis nostrud exercitation ullamco laboris nisi ut aliquip ex ea commodo consequat.</p>
      <a>Read more</a>
    </div>
    <div class="service">
      <svg width="34" height="34" viewBox="0 0 34 34"><path d="M4 2h17l6 6v22H4z" fill="none" stroke="#111" stroke-width="2.2"/><path d="M8 10h12M8 14h12M8 18h7" stroke="#111" stroke-width="2"/><circle cx="24" cy="23" r="5" fill="#111"/><path d="M21 27l-2 6 4-2M27 27l2 6-4-2" fill="#111"/></svg>
      <h3>CERTIFICATES</h3>
      <p>Lorem ipsum dolor sit amet, consectetur adipiscing elit, sed do eiusmod tempor incididunt ut labore et dolore magna aliqua. Ut enim ad minim veniam, quis nostrud exercitation ullamco laboris nisi ut aliquip ex ea commodo consequat.</p>
      <a>Read more</a>
    </div>
    <div class="service">
      <svg width="34" height="34" viewBox="0 0 34 34"><circle cx="17" cy="17" r="15" fill="#111"/><path d="M17 9v16M9 17h16" stroke="#fff" stroke-width="3"/></svg>
      <h3>MORE</h3>
      <p>Duis aute irure dolor in reprehenderit in voluptate velit esse cillum dolore eu fugiat nulla pariatur. Excepteur sint occaecat cupidatat non proident, sunt in culpa qui officia deserunt mollit anim id est laborum.</p>
      <a>Read more</a>
    </div>
  </section>

  <section class="contact">
    <h2>CONTACT US</h2>
    <div class="contact-row">
      <div>Telephone:<br>07 555 010 482</div>
      <div>Fax:<br>07 555 010 482</div>
      <div>E-mail:<br>office@brookvaleassessors.com.au</div>
      <div>Building Address:<br>Harbourline Business Centre 58 Keel Street, Qld 4700 Australia</div>
    </div>
  </section>

  <div class="map" role="img" aria-label="Street map of the office area with a location pin"></div>
  <div class="map-caption">Area Map Widget</div>

  <footer class="footer">
    <div class="footer-col">
      <h4>MENU</h4>
      <ul class="footer-menu"><li>Home</li><li>About Us</li><li>Our services</li><li>Contact Us</li></ul>
    </div>
    <div class="footer-col">
      <h4>ABOUT US</h4>
      <p>Lorem ipsum dolor sit amet, consectetur adipiscing elit, sed do eiusmod tempor incididunt ut labore et dolore magna aliqua. Ut enim ad minim veniam, quis nostrud exercitation ullamco laboris nisi ut aliquip ex ea commodo consequat. exercitation ullamco laboris nisi ut aliquip ex ea commodo consequat.</p>
    </div>
    <div class="footer-col">
      <h4>SAMPLE TEXT</h4>
      <p>Lorem ipsum dolor sit amet, consectetur adipiscing elit, sed do eiusmod tempor incididunt ut labore et dolore magna aliqua. Ut enim ad minim veniam, quis nostrud exercitation ullamco laboris nisi ut aliquip ex ea commodo consequat. quis nostrud exercitation ullamco laboris nisi ut aliquip ex ea commodo consequat.</p>
    </div>
  </footer>
  <div class="bottom-bar">
    <span><svg width="10" height="15" viewBox="0 0 10 15"><rect x="1" y="1" width="8" height="13" rx="1.5" fill="none" stroke="#2f86c6" stroke-width="1.6"/></svg>(07) 5550 1842</span>
    <span><svg width="15" height="10" viewBox="0 0 15 10"><rect width="15" height="10" fill="#2f86c6"/><path d="M0 0 7.5 6 15 0" stroke="#323232" fill="none" stroke-width="1.3"/></svg>office@brookvaleassessors.com.au</span>
    <span><svg width="10" height="14" viewBox="0 0 10 14"><path d="M5 14 0.8 6a4.2 4.2 0 1 1 8.4 0z" fill="#2f86c6"/><circle cx="5" cy="5" r="1.6" fill="#323232"/></svg>Harbourline Business Centre 58 Keel Street, Qld 4700 Australia</span>
  </div>
</div>
<div class="to-top"><svg width="10" height="6" viewBox="0 0 10 6"><path d="M1 5 5 1 9 5" fill="none" stroke="#fff" stroke-width="1.5"/></svg></div>
</body>
</html>
```